Designed the Labels for a bottle of Thornwick Gin

My com nay is The Quill Street Gin Company. We make kraft Gins and we our about to launch a new Gin Called Thornwick Gin.

The bottle to be used can be found at the following link...https://www.flaskmarten-supply.co.uk/Glass-bottles/Glass-bottles/100ml-glass-bottles/500ml-stoneware-crock-Tall-with-cork-finish-black-mat.html

I would like the front label to say Thornwick Gin with the word Lancashire vertical and Gin Horizontal. A Red Rose is the symbol for Lancashire so this needs to be woven onto the design….it could taken be red rose petals rather that a flower or bud….creatively I'd like it to have a more modern feel.

For the back label I have attached a previous label to illustrate technical information required. The works will change and the new back label may include the Lancashire Rose symbol as used by Pendlemere County Council.

Target Market(s)

UK Retail

Industry/Entity Type

It Company

Requirements
Must have
• A front and back label to fit the bottle described
Nice to have
• Modern and crisp…the bottle is black so that helps catch the eye. The label may be transparent.

```html
<!DOCTYPE html>
<html lang="en">
<head>
<meta charset="utf-8">
<title>Thornwick Gin – Front Label</title>
<link rel="stylesheet" href="https://fonts.googleapis.com/css2?family=Cormorant+Garamond:wght@400;500&family=Pinyon+Script&display=swap">
<style>
  :root {
    --label-black: #0b0b0b;
    --ink-white: #f4f4f2;
    --rose-red: #b5121b;
    --rose-deep: #6e0a10;
    --backdrop: #ffffff;
  }
  * { margin: 0; padding: 0; box-sizing: border-box; }
  html, body {
    width: 1200px; height: 1200px; overflow: hidden;
    background: var(--backdrop);
  }
  .label {
    position: absolute; left: 300px; top: 30px;
    width: 600px; height: 1140px;
    background: var(--label-black);
    border-radius: 28px;
    color: var(--ink-white);
    font-family: "Cormorant Garamond", serif;
  }
  .hand-made {
    position: absolute; top: 28px; left: 0; width: 100%;
    text-align: center; color: var(--rose-red);
    font-size: 34px; letter-spacing: 1px;
  }
  .brand-vertical {
    position: absolute; left: 82px; top: 140px;
    width: 60px;
    display: flex; flex-direction: column; align-items: center;
    font-size: 68px; line-height: 82px; font-weight: 400;
  }
  .brand-vertical span:first-child { font-size: 84px; }
  .gin-script {
    position: absolute; left: 190px; top: 120px;
    font-family: "Pinyon Script", cursive;
    font-size: 230px; line-height: 1;
    transform: rotate(-4deg);
  }
  .rose-petals {
    position: absolute; left: 182px; top: 400px;
    width: 390px; height: 430px;
  }
  .origin {
    position: absolute; top: 930px; left: 0; width: 100%;
    text-align: center;
  }
  .origin-line { font-size: 32px; letter-spacing: 1px; }
  .origin-place {
    font-family: "Pinyon Script", cursive;
    font-size: 44px; line-height: 1; margin-top: 2px;
  }
  .strength, .volume {
    position: absolute; top: 1060px; font-size: 34px;
  }
  .strength { left: 54px; }
  .volume { left: 452px; }
  .unit { font-size: 20px; letter-spacing: 1px; }
</style>
</head>
<body>
  <main class="label">
    <p class="hand-made">HAND-MADE</p>

    <h1 class="brand-vertical" aria-label="Thornwick">
      <span>T</span><span>H</span><span>O</span><span>R</span><span>N</span><span>W</span><span>I</span><span>C</span><span>K</span>
    </h1>

    <p class="gin-script">Gin</p>

    <svg class="rose-petals" viewBox="0 0 390 430" role="img" aria-label="Illustration of scattered red rose petals">
      <defs>
        <radialGradient id="petalTone" cx="50%" cy="45%" r="55%">
          <stop offset="0%" stop-color="#b5121b"/>
          <stop offset="100%" stop-color="#6e0a10"/>
        </radialGradient>
      </defs>
      <ellipse cx="195" cy="215" rx="185" ry="200" fill="url(#petalTone)" opacity="0.9"/>
    </svg>

    <div class="origin">
      <p class="origin-line">FROM THE HEART OF</p>
      <p class="origin-place">West Lancashire</p>
    </div>

    <p class="strength">42%<span class="unit">VOL</span></p>
    <p class="volume">70<span class="unit">CL</span></p>
  </main>
</body>
</html>
```